RB Larks Film Festival Poster

Design a poster for our film festival at the Redbrook University. We would like a graphic clean feel (examples attached).

Must have the following text:

18TH ANNUAL LARKS FILM FESTIVAL
MAY 1, 2 & 3 2015
OTTO VRELAND CINEMA
SCHOOL OF SCREEN AND DIGITAL STORYTELLING
REDBROOK UNIVERSITY
www.larksreelweek.example

Size:
8.5 x 10

Adobe Illustrator please.

Target Market(s)

We will print to poster size and will print to magazines.

Industry/Entity Type

Festival

Colors

Designer to choose colors to be used in the design.

```html
<!DOCTYPE html>
<html lang="en">
<head>
<meta charset="utf-8">
<title>RB Larks Film Festival Poster</title>
<link rel="stylesheet" href="https://fonts.googleapis.com/css2?family=Josefin+Sans:wght@300;400;700&display=swap">
<style>
  :root {
    --orange: #eb8249;
    --orange-deep: #c76d3b;
    --green: #7f9b6b;
    --green-deep: #637f57;
    --ink: #ffffff;
    --font: "Josefin Sans", "Helvetica Neue", Arial, sans-serif;
  }
  html, body {
    margin: 0;
    padding: 0;
    overflow: hidden;
    background: #ffffff;
  }
  .poster {
    position: relative;
    width: 1019px;
    height: 1200px;
    overflow: hidden;
    font-family: var(--font);
    color: var(--ink);
  }
  .poster__field {
    position: absolute;
    inset: 0;
    width: 100%;
    height: 100%;
  }
  .poster__url {
    position: absolute;
    top: 10px;
    left: 133px;
    margin: 0;
    font-size: 23px;
    font-weight: 300;
    letter-spacing: 1.5px;
  }
  .date-badge {
    position: absolute;
    left: 771px;
    top: 25px;
    width: 250px;
    height: 250px;
    border-radius: 50%;
    background: var(--orange);
    display: flex;
    flex-direction: column;
    align-items: center;
    justify-content: center;
    text-align: center;
    font-weight: 300;
    font-size: 27px;
    line-height: 1.2;
  }
  .date-badge__year,
  .date-badge__days {
    padding: 4px 12px;
    border-bottom: 2px solid var(--ink);
  }
  .date-badge__venue { padding-top: 6px; }
  .festival-title {
    position: absolute;
    left: 300px;
    top: 400px;
    width: 440px;
    margin: 0;
    text-align: center;
    font-weight: 400;
    font-size: 46px;
    line-height: 1.15;
    letter-spacing: 4px;
  }
  .festival-title__name {
    display: block;
    font-size: 84px;
    letter-spacing: 10px;
  }
  .host {
    position: absolute;
    left: 50px;
    top: 1015px;
    font-weight: 300;
    font-size: 24px;
    line-height: 1.45;
    letter-spacing: 0.5px;
  }
  .host__rule {
    width: 182px;
    height: 2px;
    margin: 0 0 10px 86px;
    background: var(--ink);
  }
  .host__school { margin: 0; }
  .host__divider {
    width: 360px;
    height: 2px;
    margin: 8px 0 8px 0;
    background: var(--ink);
  }
  .host__university { margin: 0 0 0 18px; }
</style>
</head>
<body>
  <main class="poster">
    <svg class="poster__field" viewBox="0 0 614 720" preserveAspectRatio="none" aria-hidden="true">
      <rect width="614" height="720" fill="var(--orange)"/>
      <polygon points="0,0 614,0 614,720" fill="var(--green)"/>
      <polygon points="382,0 614,0 614,720" fill="var(--green-deep)"/>
      <polygon points="0,435 614,720 0,720" fill="var(--orange-deep)"/>
    </svg>

    <p class="poster__url">www.larksreelweek.example</p>

    <div class="date-badge">
      <span class="date-badge__year">2015</span>
      <span class="date-badge__days">MAY 1,2&amp;3</span>
      <span class="date-badge__venue">OTTO VRELAND<br>CINEMA</span>
    </div>

    <h1 class="festival-title">
      18TH ANNUAL
      <span class="festival-title__name">LARKS</span>
      FILM FESTIVAL
    </h1>

    <footer class="host">
      <div class="host__rule"></div>
      <p class="host__school">SCHOOL OF SCREEN AND<br>DIGITAL STORYTELLING</p>
      <div class="host__divider"></div>
      <p class="host__university">REDBROOK UNIVERSITY</p>
    </footer>
  </main>
</body>
</html>
```